Consultant Word Template Design

I want to use a word template to submit service proposals to clients. You can visit my web site: Bridgewaveadvisory.com for content/ design ideas and I am also attaching my flyer. The color scheme should be consistent with my logo, web, flyer, etc. blue and white. I want some core pages: front & back page design, about us, services

Industry/Entity Type

Health Care

Colors

Designer to choose colors to be used in the design.

```html
<!DOCTYPE html>
<html lang="en">
<head>
<meta charset="UTF-8">
<title>Proposal Cover</title>
<link rel="stylesheet" href="https://fonts.googleapis.com/css2?family=Poppins:wght@600;800&display=swap">
<style>
  :root {
    --frame: #000000;
    --paper: #ffffff;
    --brand-blue: #0a4ea3;
    --band-text: #ffffff;
    --scene-window: #eef1f3;
    --scene-glass: #d6dadd;
    --scene-table: #f4f5f6;
    --scene-seat: #b3274a;
    --scene-floor: #9a9ea3;
    --scene-suit: #4a4f58;
  }
  * { margin: 0; padding: 0; box-sizing: border-box; }
  html, body { width: 850px; height: 1200px; overflow: hidden; background: var(--frame); }
  .cover {
    position: relative;
    width: 850px;
    height: 1200px;
    background: var(--frame);
    padding: 19px;
    font-family: "Poppins", sans-serif;
  }
  .page {
    position: relative;
    width: 812px;
    height: 1162px;
    background: var(--paper);
    overflow: hidden;
  }
  .hero-photo {
    position: absolute;
    left: 0; top: 0;
    width: 812px;
    height: 600px;
    background: linear-gradient(180deg,
      var(--scene-window) 0%,
      var(--scene-glass) 30%,
      var(--scene-table) 50%,
      var(--scene-suit) 62%,
      var(--scene-seat) 75%,
      var(--scene-floor) 88%,
      var(--scene-glass) 100%);
  }
  .tagline-band {
    position: absolute;
    left: 0; top: 606px;
    width: 812px;
    height: 85px;
    background: var(--brand-blue);
    display: flex;
    align-items: center;
    justify-content: center;
  }
  .tagline {
    color: var(--band-text);
    font-weight: 800;
    font-size: 31px;
    letter-spacing: 0;
    text-transform: uppercase;
    white-space: nowrap;
  }
  .band-pointer {
    position: absolute;
    left: 373px; top: 690px;
    width: 66px; height: 35px;
  }
  .project-title {
    position: absolute;
    left: 0; top: 766px;
    width: 812px;
    text-align: center;
    color: var(--brand-blue);
    font-weight: 600;
    font-size: 50px;
    line-height: 62px;
  }
  .project-subtitle {
    position: absolute;
    left: 0; top: 842px;
    width: 812px;
    text-align: center;
    color: var(--brand-blue);
    font-weight: 600;
    font-size: 31px;
    line-height: 42px;
  }
  .brand {
    position: absolute;
    left: 0; top: 985px;
    width: 812px;
    display: flex;
    align-items: center;
    justify-content: center;
    gap: 16px;
  }
  .brand-mark {
    width: 34px; height: 34px;
    border-radius: 50%;
    background: var(--brand-blue);
  }
  .brand-name {
    color: var(--brand-blue);
    font-weight: 600;
    font-size: 32px;
  }
</style>
</head>
<body>
  <div class="cover">
    <div class="page">
      <div class="hero-photo" role="img" aria-label="Photo of four medical professionals in white coats and business attire talking around a high white table on crimson stools in a bright office"></div>
      <div class="tagline-band">
        <p class="tagline">Expertise your medical practice deserves</p>
      </div>
      <svg class="band-pointer" viewBox="0 0 66 35" aria-hidden="true">
        <polygon points="0,0 66,0 33,35" fill="var(--brand-blue)"/>
      </svg>
      <h1 class="project-title">Project Title goes here</h1>
      <h2 class="project-subtitle">Project Subtitle goes here</h2>
      <div class="brand">
        <span class="brand-mark"></span>
        <span class="brand-name">Bridgewave Advisory LLC</span>
      </div>
    </div>
  </div>
</body>
</html>
```